Billboard Design for Modern Dispensary

Hello!
We need a eye-catching 12' x 24' billboard designed for a very successful, modern cannabis dispensary on the Oregon coast, United States. Because of rules, we cannot have any marijuana leafs or other cannabis related images (flower, joints, smoke, etc). We can use the words "Shop" or "Dispensary" - we cannot use the words "cannabis", "marijuana".

Some ideas we had are 3 words stacked on left or center of billboard - maybe across bottom we have horizontal logo and the following words - “North of Harbor in Gull Cove”
Another idea is to have a small bubble in bottom/top corner with image of our dog (face only) - with some words around it - like "BONUS Shop Dog" or "Cute Shop Dog" or "Best Shop Dog" or "Friendly Staff"

here's some 3 word examples:
ENJOY
YOUR
TRIP

or

FEEL
GOOD
JUST
AHEAD

or

GOOD
VIBES
ONLY

or

GOOD
TIMES
CHILL
VIBES

I have attached our logo. I have also included a stacked logo version (vertical, not horizontal). the formats are .EPS and .PDF - the logos were created in Affinity Design 2.x.

Our website is coralnook.net if you want to see more images, etc about our dispensary.

Artwork Requirements:
The billboard is 12' tall x 25' wide
The artwork needs to be 1”=1’ @ 300dpi
Please add 6” of bleed all around so your total artwork is 13”x26”
Final deliverable should be .Ai file.

Font styles to use
Sans Serif

Colors
0054AA
0677BA
7BADD7
CADEEF
E8F1F8

Requirements
Nice to have
• See the project description - we included some ideas to consider.
Should not have
• No cannabis images, like flower, cannabis leaves, paraphenlia, cartridges, joints, etc.

```html
<!DOCTYPE html>
<html lang="en">
<head>
<meta charset="utf-8">
<title>Sleep Better Tonight – Coral Nook Billboard</title>
<link rel="stylesheet" href="https://fonts.googleapis.com/css2?family=Oswald:wght@300;500;700&display=swap">
<style>
  :root {
    --ink: #0d0d0d;
    --accent: #3f9ad6;
    --mist-top: #f4f7fa;
    --mist-mid: #e3ebf2;
    --mist-low: #c9d3dc;
    --ridge: #b3bcc5;
    --text-dark: #1b1b1b;
  }
  html, body {
    margin: 0;
    padding: 0;
    width: 1200px;
    height: 1105px;
    overflow: hidden;
    background: #ffffff;
  }
  .billboard {
    position: relative;
    width: 1200px;
    height: 1105px;
    overflow: hidden;
    font-family: "Oswald", "Arial Narrow", sans-serif;
  }
  .backdrop {
    position: absolute;
    inset: 0;
    background:
      radial-gradient(ellipse 70% 35% at 60% 95%, var(--ridge) 0%, rgba(179,188,197,0) 70%),
      radial-gradient(ellipse 40% 45% at 12% 88%, var(--mist-low) 0%, rgba(201,211,220,0) 75%),
      linear-gradient(180deg, var(--mist-top) 0%, var(--mist-mid) 55%, #d9e2ea 100%);
  }
  .headline {
    position: absolute;
    left: 0;
    top: 0;
    width: 100%;
    margin: 0;
    font-weight: 700;
    color: var(--ink);
    text-transform: uppercase;
  }
  .headline .line {
    position: absolute;
    left: 0;
    width: 100%;
    text-align: center;
    line-height: 1;
    white-space: nowrap;
    transform-origin: 50% 0;
  }
  .line-sleep   { top: 41px;  font-size: 161px; letter-spacing: 4px; transform: scaleX(1.48); }
  .line-better  { top: 219px; font-size: 220px; letter-spacing: 6px; transform: scaleX(1.0); }
  .line-tonight { top: 452px; font-size: 215px; letter-spacing: 5px; transform: scaleX(1.14); }
  .accent-letter { color: var(--accent); }
  .brand-mark {
    position: absolute;
    left: 276px;
    top: 786px;
    width: 162px;
    height: 162px;
    border-radius: 50%;
    background: var(--accent);
  }
  .brand-name {
    position: absolute;
    left: 456px;
    top: 815px;
    margin: 0;
    font-weight: 300;
    font-size: 66px;
    letter-spacing: 9px;
    color: var(--text-dark);
    line-height: 1;
    text-transform: uppercase;
    white-space: nowrap;
  }
  .location {
    position: absolute;
    left: 0;
    top: 976px;
    width: 100%;
    margin: 0;
    text-align: center;
    font-weight: 500;
    font-size: 57px;
    line-height: 1;
    color: var(--text-dark);
    text-transform: uppercase;
    letter-spacing: 3px;
    white-space: nowrap;
  }
</style>
</head>
<body>
  <main class="billboard">
    <div class="backdrop" role="img" aria-label="Misty blue mountain range with a hiker standing on a summit, arms raised"></div>
    <h1 class="headline">
      <span class="line line-sleep">Sleep</span>
      <span class="line line-better">Better</span>
      <span class="line line-tonight">T<span class="accent-letter">o</span>night</span>
    </h1>
    <div class="brand-mark"></div>
    <p class="brand-name">Coral Nook</p>
    <p class="location">North of Harbor in Gull Cove</p>
  </main>
</body>
</html>
```